We need a website for an ice cream shop "otter ice cream"

We are opening an ice cream shop called "otter ice cream". We already have a logo (photo attached). The ice cream shop will be in the style of "Coral Motel" movie - palm trees, sunset, there will be a flamingo on the wall, so basically sunset, beach, Miami style. We would like the website to be colorful, colors of sunset, colorful buildings, girls wearing vintage roller skates. You can get inspiration from the "Coral Motel" movie. We would like the website to be playful, a little vintage, not boring. The website should attract people's attention.

Target Market(s)

everyone

Industry/Entity Type

ice cream shop

Number of Pages Required

5+ page

Font styles to use
Sans Serif
Script

Colors
0094D4
00A9DD
6FCCEA
C7EBF8
E9F6FB
FFC000
F8CF3A
FAE287
FDF2CF
FEFAEE
F0912C
F2A743
F7CA91
FBE8D2
FDF5EE
EE7325
F08F49
F5BC92
FAE3D3
FDF4ED
E54698
E96AAD
F1A4CE
F9D9EA
FCEFF6
A7469A
B969AE
D3A5CF
EDDBEB
F8F0F9

Requirements
Must have
• tropical, Miami style, sunset
Nice to have
• palm trees, flamingo, girls on vintage roller skates, sea, colorful buildings

```html
<!DOCTYPE html>
<html lang="en">
<head>
<meta charset="utf-8">
<title>Otter Ice Cream</title>
<link href="https://fonts.googleapis.com/css2?family=Righteous&family=Delius&family=Poppins:wght@400;500;600&display=swap" rel="stylesheet">
<style>
:root{
  --ocean:#0094d4;
  --sky:#00a9dd;
  --sky-soft:#6fccea;
  --gold:#ffc000;
  --sun:#f8cf3a;
  --orange:#f0912c;
  --orange-deep:#ee7325;
  --pink:#e54698;
  --pink-soft:#f1a4ce;
  --pink-pale:#fceff6;
  --purple:#a7469a;
  --purple-soft:#d3a5cf;
  --cream:#fdf5ee;
  --sand:#fdf2cf;
  --white:#ffffff;
  --ink:#3a1f3a;
  --muted:#7a6470;
}
*{margin:0;padding:0;box-sizing:border-box}
html,body{width:1200px;height:2981px;overflow:hidden;background:var(--white)}
body{position:relative;font-family:'Delius',cursive}
.screen{position:absolute;left:0;width:1200px;height:580px;overflow:hidden}
.s1{top:0}.s2{top:600px}.s3{top:1202px}.s4{top:1800px}.s5{top:2398px}

/* sidebar */
.sidebar{position:absolute;left:0;top:0;width:227px;height:580px;
  background:linear-gradient(180deg,var(--purple) 0%,var(--pink) 38%,var(--orange) 75%,var(--gold) 100%);color:var(--white);text-align:center}
.burger{position:absolute;right:26px;top:20px;width:16px}
.burger span{display:block;height:1.5px;background:#fff;margin-bottom:4px}
.burger span:nth-child(2){width:11px;margin-left:5px}
.brand{position:absolute;left:50%;top:66px;transform:translateX(-50%);width:126px;height:126px;border-radius:50%;
  background:var(--ocean);border:3px solid var(--sun);display:flex;align-items:center;justify-content:center;
  font-family:'Righteous',sans-serif;font-size:17px;line-height:1.15;color:var(--sun)}
.nav{position:absolute;top:230px;left:0;width:100%;list-style:none;font-size:12.5px;font-weight:700}
.nav li{height:40px}
.nav li.active{color:var(--sun)}
.menu-btn{position:absolute;left:57px;top:400px;width:116px;height:40px;border:1.5px solid #fff;font-size:14px;font-weight:700;line-height:37px}
.socials{position:absolute;top:476px;left:30px;display:flex;gap:11px}
.socials span{width:35px;height:35px;border-radius:50%;background:#fff;display:flex;align-items:center;justify-content:center}
.copyright{position:absolute;top:539px;width:100%;font-size:9px}

.photo{position:absolute}

/* hero */
.hero-bg{left:227px;top:0;width:973px;height:580px;
  background:linear-gradient(120deg,#f7ca91 0%,#f08f49 28%,#e96aad 58%,#6fccea 100%)}
.hero-tint{position:absolute;left:227px;top:0;width:973px;height:580px;background:linear-gradient(180deg,rgba(167,70,154,.25),rgba(229,70,152,.2) 60%,rgba(0,148,212,.25))}
.hero-title{position:absolute;left:227px;width:973px;top:226px;text-align:center;color:#fff;
  font-family:'Righteous',sans-serif;font-size:62px;font-weight:400}
.hero-sub{position:absolute;left:227px;width:973px;top:318px;text-align:center;color:#fff;font-size:14px}
.arrow{position:absolute;top:519px;width:40px;height:40px;border-radius:50%;background:rgba(255,255,255,.6)}
.arrow svg{position:absolute;left:14px;top:14px}

/* about */
.about-bg{left:227px;top:0;width:973px;height:580px;
  background:linear-gradient(100deg,#a7469a 0%,#b969ae 35%,#e96aad 65%,#f5bc92 100%)}
.about-title{position:absolute;left:315px;top:190px;color:var(--white);font-family:'Righteous',sans-serif;font-size:24px;font-weight:400}
.about-text{position:absolute;left:314px;top:234px;width:440px;color:var(--white);font-size:14.4px;line-height:24.5px}
.about-frame{position:absolute;left:918px;top:163px;width:211px;height:235px;border:3px solid var(--gold);border-radius:6px}
.about-photo{left:905px;top:172px;width:213px;height:238px;background:linear-gradient(160deg,#f9d9ea,#e54698 55%,#a7469a)}

/* gallery */
.gallery-bg{position:absolute;left:227px;top:0;width:973px;height:580px;background:linear-gradient(180deg,var(--sand),var(--pink-pale))}
.polaroid{position:absolute;width:200px;height:234px;background:#fff;box-shadow:0 2px 6px rgba(167,70,154,.22);padding:9px}
.polaroid .pic{width:182px;height:190px}
.polaroid p{font-family:'Poppins',sans-serif;font-size:11.5px;font-weight:500;text-align:center;margin-top:7px;color:var(--ink)}

/* flavors */
.flavor-bg{position:absolute;left:227px;top:0;width:973px;height:580px;background:linear-gradient(180deg,var(--cream),#e9f6fb)}
.kicker{position:absolute;left:227px;width:973px;top:50px;text-align:center;color:var(--pink);font-size:12px}
.flavor-title{position:absolute;left:227px;width:973px;top:70px;text-align:center;font-family:'Righteous',sans-serif;font-weight:400;font-size:23px;letter-spacing:1px;color:var(--ink)}
.flavor-card{position:absolute;top:135px;width:193px;height:222px;background:#fff;border-radius:3px;padding:8px;box-shadow:0 1px 4px rgba(0,148,212,.15)}
.flavor-card .pic{width:177px;height:177px}
.flavor-card p{font-family:'Poppins',sans-serif;font-size:11.5px;text-align:center;margin-top:9px;color:var(--ink)}
.price-list{position:absolute;left:309px;top:398px;width:816px;height:190px;background:#fff;border-radius:4px}
.item{position:absolute;width:408px;height:64px}
.item .dot{position:absolute;left:22px;top:13px;width:38px;height:38px;border-radius:50%}
.item .name{position:absolute;left:70px;top:12px;font-family:'Poppins',sans-serif;font-size:13.5px;color:var(--orange-deep)}
.item .desc{position:absolute;left:70px;top:36px;font-size:10px;color:var(--muted)}
.item .price{position:absolute;right:24px;top:14px;font-family:'Poppins',sans-serif;font-weight:600;font-size:17px;color:var(--purple)}
.row-line{position:absolute;left:0;width:816px;height:1px;background:#f3e6ee}

/* contact */
.contact-bg{left:227px;top:0;width:973px;height:580px;background:linear-gradient(160deg,#3a1d4a 0%,#5a2350 50%,#2a1636 100%)}
.contact-tint{position:absolute;left:227px;top:0;width:973px;height:580px;background:rgba(20,8,30,.3)}
.talk-title{position:absolute;left:308px;top:82px;color:#fff;font-family:'Poppins',sans-serif;font-weight:500;font-size:20px}
.label{position:absolute;left:308px;color:#fff;font-size:11px}
.value{position:absolute;left:308px;color:var(--gold);font-family:'Poppins',sans-serif;font-weight:500;font-size:15px;line-height:19px}
.touch-title{position:absolute;left:658px;top:82px;color:#fff;font-family:'Poppins',sans-serif;font-weight:600;font-size:19px;letter-spacing:.5px}
.field{position:absolute;left:658px;width:466px;height:37px;border:1px solid var(--pink-soft);border-radius:18px;color:#fff;font-size:11.5px;padding:10px 12px}
.field.message{height:93px;border-radius:16px}
.submit{position:absolute;left:658px;top:446px;width:106px;height:38px;border:1px solid var(--pink-soft);background:var(--pink);border-radius:19px;color:#fff;font-size:12px;text-align:center;line-height:36px}
</style>
</head>
<body>

<!-- Screen 1: hero -->
<section class="screen s1">
  <div class="photo hero-bg" role="img" aria-label="Photo of an ice cream cone held in front of a shop counter"></div>
  <div class="hero-tint"></div>
  <h1 class="hero-title">Welcome to Otter ice</h1>
  <p class="hero-sub">we have over 300 delicious flavours for you to choose, come and visit our shop today!</p>
  <div class="arrow" style="left:1081px"><svg width="12" height="12" viewBox="0 0 12 12"><path d="M8 2 4 6l4 4" fill="none" stroke="#a7469a" stroke-width="2"/></svg></div>
  <div class="arrow" style="left:1132px"><svg width="12" height="12" viewBox="0 0 12 12"><path d="M4 2l4 4-4 4" fill="none" stroke="#a7469a" stroke-width="2"/></svg></div>
  <aside class="sidebar">
    <div class="burger"><span></span><span></span><span></span></div>
    <div class="brand">Otter<br>Ice Cream</div>
    <ul class="nav"><li class="active">Home</li><li>About</li><li>Photos</li><li>Contact us</li></ul>
    <div class="menu-btn">Menu</div>
    <div class="socials">
      <span><svg width="14" height="14" viewBox="0 0 14 14"><path d="M3 1h3l1 3-2 1.5a7 7 0 0 0 3.5 3.5L10 7l3 1v3a2 2 0 0 1-2 2A10 10 0 0 1 1 3a2 2 0 0 1 2-2z" fill="#e54698"/></svg></span>
      <span><svg width="14" height="14" viewBox="0 0 14 14"><path d="M7 13s-4.5-4.5-4.5-7.5a4.5 4.5 0 0 1 9 0C11.5 8.5 7 13 7 13z" fill="#f0912c"/><circle cx="7" cy="5.5" r="1.6" fill="#fff"/></svg></span>
      <span><svg width="14" height="14" viewBox="0 0 14 14"><rect x="1" y="3" width="12" height="8" rx="1" fill="none" stroke="#0094d4" stroke-width="1.5"/><path d="M1.5 3.5 7 8l5.5-4.5" fill="none" stroke="#0094d4" stroke-width="1.5"/></svg></span>
      <span><svg width="14" height="14" viewBox="0 0 14 14"><path d="M2 7.5 5.5 11 12 3.5" fill="none" stroke="#a7469a" stroke-width="2"/></svg></span>
    </div>
    <p class="copyright">Copyright © 2022, All Rights Reserved</p>
  </aside>
</section>

<!-- Screen 2: about -->
<section class="screen s2">
  <div class="photo about-bg" role="img" aria-label="Photo of ice cream, strawberries and flowers on a marble table with a tinted overlay"></div>
  <h2 class="about-title">About Otter Ice</h2>
  <p class="about-text">Lorem ipsum dolor sit amet, consectetur adipiscing elit. Suspendisse varius enim in eros elementum tristique. Duis cursus, mi quis viverra ornare, eros dolor interdum nulla, ut commodo diam libero vitae erat. Aenean faucibus nibh et justo cursus id rutrum lorem imperdiet. Nunc ut sem vitae risus tristique posuere.</p>
  <div class="about-frame"></div>
  <div class="photo about-photo" role="img" aria-label="Photo of a woman in sunglasses holding an ice cream cone"></div>
  <aside class="sidebar">
    <div class="burger"><span></span><span></span><span></span></div>
    <div class="brand">Otter<br>Ice Cream</div>
    <ul class="nav"><li class="active">Home</li><li>About</li><li>Photos</li><li>Contact us</li></ul>
    <div class="menu-btn">Menu</div>
    <div class="socials">
      <span><svg width="14" height="14" viewBox="0 0 14 14"><path d="M3 1h3l1 3-2 1.5a7 7 0 0 0 3.5 3.5L10 7l3 1v3a2 2 0 0 1-2 2A10 10 0 0 1 1 3a2 2 0 0 1 2-2z" fill="#e54698"/></svg></span>
      <span><svg width="14" height="14" viewBox="0 0 14 14"><path d="M7 13s-4.5-4.5-4.5-7.5a4.5 4.5 0 0 1 9 0C11.5 8.5 7 13 7 13z" fill="#f0912c"/><circle cx="7" cy="5.5" r="1.6" fill="#fff"/></svg></span>
      <span><svg width="14" height="14" viewBox="0 0 14 14"><rect x="1" y="3" width="12" height="8" rx="1" fill="none" stroke="#0094d4" stroke-width="1.5"/><path d="M1.5 3.5 7 8l5.5-4.5" fill="none" stroke="#0094d4" stroke-width="1.5"/></svg></span>
      <span><svg width="14" height="14" viewBox="0 0 14 14"><path d="M2 7.5 5.5 11 12 3.5" fill="none" stroke="#a7469a" stroke-width="2"/></svg></span>
    </div>
    <p class="copyright">Copyright © 2022, All Rights Reserved</p>
  </aside>
</section>

<!-- Screen 3: photo gallery -->
<section class="screen s3">
  <div class="gallery-bg"></div>
  <div class="polaroid" style="left:305px;top:44px;transform:rotate(3deg)"><div class="pic" role="img" aria-label="Photo of ice cream cups with sprinkles and cones" style="background:linear-gradient(160deg,#f9d9ea,#e96aad 50%,#f8cf3a)"></div><p>Our famous Petit four</p></div>
  <div class="polaroid" style="left:510px;top:44px;transform:rotate(3deg)"><div class="pic" role="img" aria-label="Photo of chocolate ice cream scoops in a pineapple" style="background:linear-gradient(160deg,#fbe8d2,#f2a743 50%,#ffc000)"></div><p>Delicious Cupcakes</p></div>
  <div class="polaroid" style="left:716px;top:44px;transform:rotate(3deg)"><div class="pic" role="img" aria-label="Photo of a plated dessert with berries" style="background:linear-gradient(160deg,#e9f6fb,#c7ebf8 55%,#b969ae)"></div><p>Our famous Petit four</p></div>
  <div class="polaroid" style="left:921px;top:44px;transform:rotate(3deg)"><div class="pic" role="img" aria-label="Photo of a woman holding an ice cream cone" style="background:linear-gradient(160deg,#f9d9ea,#e54698 60%,#a7469a)"></div><p>Delicious Cupcakes</p></div>
  <div class="polaroid" style="left:305px;top:306px;transform:rotate(3deg)"><div class="pic" role="img" aria-label="Photo of a woman holding an ice cream cone" style="background:linear-gradient(160deg,#f9d9ea,#e54698 60%,#a7469a)"></div><p>Delicious Cupcakes</p></div>
  <div class="polaroid" style="left:510px;top:306px;transform:rotate(3deg)"><div class="pic" role="img" aria-label="Photo of a rainbow soft serve cone" style="background:linear-gradient(160deg,#6fccea,#f1a4ce 45%,#fae287)"></div><p>Our famous Petit four</p></div>
  <div class="polaroid" style="left:716px;top:306px;transform:rotate(3deg)"><div class="pic" role="img" aria-label="Photo of a colourful ice cream sundae" style="background:linear-gradient(160deg,#00a9dd,#f8cf3a 50%,#e54698)"></div><p>Delicious Cupcakes</p></div>
  <div class="polaroid" style="left:921px;top:306px;transform:rotate(3deg)"><div class="pic" role="img" aria-label="Photo of a hand holding an ice cream cone" style="background:linear-gradient(160deg,#fdf4ed,#f5bc92 50%,#e96aad)"></div><p>Our famous Petit four</p></div>
  <div class="polaroid" style="left:305px;top:566px;transform:rotate(3deg)"><div class="pic" style="background:#e96aad"></div></div>
  <div class="polaroid" style="left:510px;top:566px;transform:rotate(3deg)"><div class="pic" style="background:#6fccea"></div></div>
  <div class="polaroid" style="left:716px;top:566px;transform:rotate(3deg)"><div class="pic" style="background:#d3a5cf"></div></div>
  <div class="polaroid" style="left:921px;top:566px;transform:rotate(3deg)"><div class="pic" style="background:#f08f49"></div></div>
  <aside class="sidebar">
    <div class="burger"><span></span><span></span><span></span></div>
    <div class="brand">Otter<br>Ice Cream</div>
    <ul class="nav"><li class="active">Home</li><li>About</li><li>Photos</li><li>Contact us</li></ul>
    <div class="menu-btn">Menu</div>
    <div class="socials">
      <span><svg width="14" height="14" viewBox="0 0 14 14"><path d="M3 1h3l1 3-2 1.5a7 7 0 0 0 3.5 3.5L10 7l3 1v3a2 2 0 0 1-2 2A10 10 0 0 1 1 3a2 2 0 0 1 2-2z" fill="#e54698"/></svg></span>
      <span><svg width="14" height="14" viewBox="0 0 14 14"><path d="M7 13s-4.5-4.5-4.5-7.5a4.5 4.5 0 0 1 9 0C11.5 8.5 7 13 7 13z" fill="#f0912c"/><circle cx="7" cy="5.5" r="1.6" fill="#fff"/></svg></span>
      <span><svg width="14" height="14" viewBox="0 0 14 14"><rect x="1" y="3" width="12" height="8" rx="1" fill="none" stroke="#0094d4" stroke-width="1.5"/><path d="M1.5 3.5 7 8l5.5-4.5" fill="none" stroke="#0094d4" stroke-width="1.5"/></svg></span>
      <span><svg width="14" height="14" viewBox="0 0 14 14"><path d="M2 7.5 5.5 11 12 3.5" fill="none" stroke="#a7469a" stroke-width="2"/></svg></span>
    </div>
    <p class="copyright">Copyright © 2022, All Rights Reserved</p>
  </aside>
</section>

<!-- Screen 4: flavors -->
<section class="screen s4">
  <div class="flavor-bg"></div>
  <p class="kicker">our flavors</p>
  <h2 class="flavor-title">TASTE OUR DELISH FLAVORS</h2>
  <div class="flavor-card" style="left:309px"><div class="pic" role="img" aria-label="Photo of pink frosted cupcakes" style="background:linear-gradient(160deg,#fcef f6,#f1a4ce 55%,#e54698)"></div><p>PISTACHIO</p></div>
  <div class="flavor-card" style="left:517px"><div class="pic" role="img" aria-label="Photo of assorted petit fours" style="background:linear-gradient(160deg,#fae287,#f2a743 50%,#ee7325)"></div><p>RASPBERRY</p></div>
  <div class="flavor-card" style="left:725px"><div class="pic" role="img" aria-label="Photo of cupcakes with blue and pink frosting" style="background:linear-gradient(160deg,#c7ebf8,#6fccea 50%,#f1a4ce)"></div><p>VANILLA</p></div>
  <div class="flavor-card" style="left:933px"><div class="pic" role="img" aria-label="Photo of layered cake with red berries" style="background:linear-gradient(160deg,#0094d4,#fdf2cf 55%,#e54698)"></div><p>CHOCOLATE</p></div>
  <div class="price-list">
    <div class="row-line" style="top:64px"></div>
    <div class="row-line" style="top:128px"></div>
    <div class="item" style="left:0;top:0"><div class="dot" role="img" aria-label="Photo of pistachio ice cream" style="background:#f1a4ce"></div><span class="name">PISTACHIO</span><span class="desc">Lorem ipsum dolor sit amet consectetur adipiscing</span><span class="price">$4.50</span></div>
    <div class="item" style="left:408px;top:0"><div class="dot" role="img" aria-label="Photo of strawberry ice cream" style="background:#e54698"></div><span class="name">STRAWBERRY</span><span class="desc">Lorem ipsum dolor sit amet consectetur adipiscing</span><span class="price">$4.99</span></div>
    <div class="item" style="left:0;top:64px"><div class="dot" role="img" aria-label="Photo of raspberry ice cream" style="background:#b969ae"></div><span class="name">RASPBERRY</span><span class="desc">Lorem ipsum dolor sit amet consectetur adipiscing</span><span class="price">$2.55</span></div>
    <div class="item" style="left:408px;top:64px"><div class="dot" role="img" aria-label="Photo of plum ice cream" style="background:#a7469a"></div><span class="name">PLUM</span><span class="desc">Lorem ipsum dolor sit amet consectetur adipiscing</span><span class="price">$2.55</span></div>
    <div class="item" style="left:0;top:128px"><div class="dot" role="img" aria-label="Photo of vanilla ice cream" style="background:#fae287"></div><span class="name">VANILLA</span><span class="desc">Lorem ipsum dolor sit amet consectetur adipiscing</span><span class="price">$2.55</span></div>
    <div class="item" style="left:408px;top:128px"><div class="dot" role="img" aria-label="Photo of coconut ice cream" style="background:#6fccea"></div><span class="name">COCONUT</span><span class="desc">Lorem ipsum dolor sit amet consectetur adipiscing</span><span class="price">$2.55</span></div>
  </div>
  <aside class="sidebar">
    <div class="burger"><span></span><span></span><span></span></div>
    <div class="brand">Otter<br>Ice Cream</div>
    <ul class="nav"><li class="active">Home</li><li>About</li><li>Photos</li><li>Contact us</li></ul>
    <div class="menu-btn">Menu</div>
    <div class="socials">
      <span><svg width="14" height="14" viewBox="0 0 14 14"><path d="M3 1h3l1 3-2 1.5a7 7 0 0 0 3.5 3.5L10 7l3 1v3a2 2 0 0 1-2 2A10 10 0 0 1 1 3a2 2 0 0 1 2-2z" fill="#e54698"/></svg></span>
      <span><svg width="14" height="14" viewBox="0 0 14 14"><path d="M7 13s-4.5-4.5-4.5-7.5a4.5 4.5 0 0 1 9 0C11.5 8.5 7 13 7 13z" fill="#f0912c"/><circle cx="7" cy="5.5" r="1.6" fill="#fff"/></svg></span>
      <span><svg width="14" height="14" viewBox="0 0 14 14"><rect x="1" y="3" width="12" height="8" rx="1" fill="none" stroke="#0094d4" stroke-width="1.5"/><path d="M1.5 3.5 7 8l5.5-4.5" fill="none" stroke="#0094d4" stroke-width="1.5"/></svg></span>
      <span><svg width="14" height="14" viewBox="0 0 14 14"><path d="M2 7.5 5.5 11 12 3.5" fill="none" stroke="#a7469a" stroke-width="2"/></svg></span>
    </div>
    <p class="copyright">Copyright © 2022, All Rights Reserved</p>
  </aside>
</section>

<!-- Screen 5: contact -->
<section class="screen s5">
  <div class="photo contact-bg" role="img" aria-label="Dark photo of a slice of berry cake"></div>
  <div class="contact-tint"></div>
  <h2 class="talk-title">Let's talk</h2>
  <p class="label" style="top:134px">Contact Number :</p>
  <p class="value" style="top:154px;color:var(--orange)">+44 141 555 0187</p>
  <p class="label" style="top:199px">Got a ice product to discuss?</p>
  <p class="value" style="top:216px">hello@otterscoops.example</p>
  <p class="label" style="top:258px">Would you like to share</p>
  <p class="value" style="top:275px">Harbour Lodge 14 Palm Row,<br>Seabrook Bay, SB4 2QT</p>
  <h2 class="touch-title">GET IN TOUCH</h2>
  <div class="field" style="top:124px">Enter Your Name</div>
  <div class="field" style="top:186px">Enter Your Email</div>
  <div class="field" style="top:248px">Enter Your Phone</div>
  <div class="field message" style="top:310px">Message</div>
  <div class="submit">Submit</div>
  <aside class="sidebar">
    <div class="burger"><span></span><span></span><span></span></div>
    <div class="brand">Otter<br>Ice Cream</div>
    <ul class="nav"><li class="active">Home</li><li>About</li><li>Photos</li><li>Contact us</li></ul>
    <div class="menu-btn">Menu</div>
    <div class="socials">
      <span><svg width="14" height="14" viewBox="0 0 14 14"><path d="M3 1h3l1 3-2 1.5a7 7 0 0 0 3.5 3.5L10 7l3 1v3a2 2 0 0 1-2 2A10 10 0 0 1 1 3a2 2 0 0 1 2-2z" fill="#e54698"/></svg></span>
      <span><svg width="14" height="14" viewBox="0 0 14 14"><path d="M7 13s-4.5-4.5-4.5-7.5a4.5 4.5 0 0 1 9 0C11.5 8.5 7 13 7 13z" fill="#f0912c"/><circle cx="7" cy="5.5" r="1.6" fill="#fff"/></svg></span>
      <span><svg width="14" height="14" viewBox="0 0 14 14"><rect x="1" y="3" width="12" height="8" rx="1" fill="none" stroke="#0094d4" stroke-width="1.5"/><path d="M1.5 3.5 7 8l5.5-4.5" fill="none" stroke="#0094d4" stroke-width="1.5"/></svg></span>
      <span><svg width="14" height="14" viewBox="0 0 14 14"><path d="M2 7.5 5.5 11 12 3.5" fill="none" stroke="#a7469a" stroke-width="2"/></svg></span>
    </div>
    <p class="copyright">Copyright © 2022, All Rights Reserved</p>
  </aside>
</section>

</body>
</html>
```